Website re-design for Birchmont LLC website ( has existing website )

Looking to do a complete re-design of Birchmontllc. The existing website is dated and built in wordpress. The new website will not be wordpress. The project folder includes an overview.txt file with details on the project. The file also contains a list of websites that he/she likes which I am sure is very helpful .
Number of Pages Required
1 page

```html
<!DOCTYPE html>
<html lang="en">
<head>
<meta charset="utf-8">
<title>Birchmont LLC</title>
<link href="https://fonts.googleapis.com/css2?family=Montserrat:wght@400;500;600;700&family=Barlow:ital,wght@0,400;0,500;0,600;1,400&display=swap" rel="stylesheet">
<style>
:root{
  --blue:#1f6fd1;
  --blue-dark:#0d5bb5;
  --blue-deep:#0a4fa8;
  --orange:#ff7a0d;
  --ink:#1f2a3a;
  --text:#4a5160;
  --muted:#7b8290;
  --band:#e8f0fa;
  --white:#ffffff;
  --line:#c9d3df;
}
*{margin:0;padding:0;box-sizing:border-box}
html,body{width:1200px;height:4619px;overflow:hidden;background:var(--white)}
body{position:relative;font-family:'Barlow',sans-serif;color:var(--text)}
.abs{position:absolute}
.heading{font-family:'Montserrat',sans-serif;color:var(--ink);font-weight:500}
.rule{display:block;width:74px;height:6px;border-top:2px solid var(--blue);border-bottom:2px solid var(--line);margin:12px auto 0}
.btn{position:absolute;display:flex;align-items:center;justify-content:center;border-radius:30px;font-family:'Montserrat',sans-serif;font-weight:600;font-size:13px;letter-spacing:.3px}
.btn-solid{background:var(--blue-dark);color:#fff}
.btn-orange{background:var(--orange);color:#fff}
.btn-outline{border:2px solid var(--blue-dark);color:var(--blue-dark);background:#fff;font-size:11px}

/* nav */
.site-nav{position:absolute;left:0;top:0;width:1200px;height:93px;background:#fff}
.brand{position:absolute;left:75px;top:12px;display:flex;align-items:center;gap:12px}
.brand-dot{width:70px;height:70px;border-radius:50%;background:var(--blue)}
.brand-name{font-family:'Montserrat',sans-serif;font-weight:500;font-size:34px;color:var(--blue)}
.nav-links{position:absolute;left:402px;top:36px;display:flex;gap:34px;font-family:'Barlow',sans-serif;font-size:16px;color:var(--ink)}
.nav-links .active{color:var(--blue)}
.nav-cta{left:1006px;top:27px;width:136px;height:38px;font-weight:500;font-size:15px}

/* hero */
.hero{position:absolute;left:0;top:93px;width:1200px;height:603px;background:linear-gradient(180deg,#5f7458 0%,#4d6a5b 40%,#3e5c58 75%,#4a6560 100%)}
.hero-eyebrow{position:absolute;left:0;width:1200px;top:183px;text-align:center;font-family:'Montserrat',sans-serif;font-size:24px;color:#fff;letter-spacing:1px}
.hero-title{position:absolute;left:0;width:1200px;top:218px;text-align:center;font-family:'Montserrat',sans-serif;font-weight:600;font-size:47px;line-height:52px;color:#fff}
.hero-btn{left:502px;top:340px;width:180px;height:50px;font-size:14px}

/* feature circles */
.feature{position:absolute;border-radius:50%;display:flex;flex-direction:column;align-items:center;justify-content:center;text-align:center;color:#fff;background:radial-gradient(circle at 50% 40%,#4a9be8,#1e72d4 70%)}
.feature.main{border:6px solid #fff;box-shadow:0 0 0 5px var(--blue-deep);background:radial-gradient(circle at 50% 40%,#3e8ee0,#1a66c4 70%)}
.feature h3{font-family:'Montserrat',sans-serif;font-size:20px;line-height:24px;font-weight:700}
.feature h3 span{font-weight:400;display:block}
.feature p{font-size:13px;line-height:20px;width:230px;margin-top:10px;opacity:.9}
.feature svg{margin-top:16px}

/* about */
.about-media{left:108px;top:1037px;width:476px;height:326px;background:linear-gradient(180deg,#e8a45a 0%,#c77b4a 45%,#2d3040 60%,#1b1e28 100%)}
.about-title{left:632px;top:1033px;font-size:31px;line-height:38px;font-weight:600}
.about-title .rule{margin:10px 0 0 28px}
.about-copy{left:632px;top:1138px;width:480px;font-size:16px;line-height:27px}
.about-btn{left:632px;top:1322px;width:150px;height:42px}

/* services */
.services{position:absolute;left:0;top:1475px;width:1200px;height:1116px;background:var(--band)}
.section-title{position:absolute;left:0;width:1200px;text-align:center;font-size:31px}
.card{position:absolute;width:319px;height:401px;background:#fff;text-align:center}
.card .photo{height:219px}
.card h4{font-family:'Montserrat',sans-serif;font-weight:600;font-size:16px;line-height:21px;color:var(--ink);margin-top:24px}
.card p{font-size:13px;line-height:19px;color:var(--muted);width:270px;margin:8px auto 0}
.card .btn{position:relative;width:140px;height:36px;margin:14px auto 0}
.view-all{left:493px;top:1012px;width:225px;height:46px;font-size:14px}

/* gallery */
.slide{position:absolute}
.arrow{position:absolute}

/* testimonials */
.testimonials{position:absolute;left:0;top:3140px;width:1200px;height:512px;background:linear-gradient(180deg,#3b82d6,#2169c4 60%,#1c62be)}
.testimonials .section-title{color:#fff;font-size:34px}
.quote-card{position:absolute;left:283px;top:179px;width:610px;height:265px;background:#fff;border-radius:4px;text-align:center}
.quote-badge{position:absolute;left:561px;top:152px;width:56px;height:56px;border-radius:50%;background:#5a9ae0;display:flex;align-items:center;justify-content:center}
.quote-text{font-style:italic;font-size:17px;line-height:23px;color:var(--ink);width:500px;margin:64px auto 0}
.quote-name{font-family:'Montserrat',sans-serif;font-weight:600;font-size:13px;color:var(--ink);margin-top:18px}
.quote-place{font-size:13px;color:var(--ink);margin-top:6px}

/* contact */
.contact{position:absolute;left:0;top:3652px;width:1200px;height:567px;background:linear-gradient(180deg,#f3f6fa,#e7edf4)}
.contact-title{left:135px;top:110px;font-size:34px;font-weight:500}
.contact-title .rule{margin:10px 0 0 0}
.contact-intro{left:135px;top:196px;width:380px;font-size:14px;line-height:23px;color:var(--muted)}
.info-row{position:absolute;left:135px;display:flex;gap:20px}
.info-icon{width:50px;height:50px;border-radius:50%;background:var(--blue-dark);display:flex;align-items:center;justify-content:center}
.info-label{font-size:13px;color:var(--muted);letter-spacing:.3px}
.info-value{font-size:21px;color:var(--ink);line-height:32px}
.form-card{position:absolute;left:606px;top:92px;width:479px;height:370px;background:#fff;box-shadow:0 4px 20px rgba(0,0,0,.06)}
.field{position:absolute;left:45px;width:398px;height:44px;border:1.5px solid var(--line);display:flex;align-items:center;gap:10px;padding-left:16px;font-size:13px;color:var(--ink)}
.field.area{height:80px;align-items:flex-start;padding-top:14px}
.form-btn{left:42px;top:300px;width:150px;height:40px;font-size:12px}

/* footer */
.footer{position:absolute;left:0;top:4219px;width:1200px;height:400px;background:#fff}
.f-brand{left:116px;top:65px}
.f-brand .brand-dot{width:60px;height:60px}
.f-brand .brand-name{font-size:30px}
.f-about{left:122px;top:142px;width:300px;font-size:12px;line-height:19px}
.socials{left:122px;top:222px;display:flex;gap:14px}
.socials span{width:28px;height:28px;border-radius:50%;background:var(--blue-dark)}
.f-col-title{font-family:'Montserrat',sans-serif;font-weight:600;font-size:17px;color:var(--ink);padding-left:22px;border-left:3px solid var(--blue)}
.f-links{display:grid;grid-template-columns:137px 130px;row-gap:14px;font-size:14px;margin-top:18px;padding-left:25px}
.f-contact{margin-top:18px;padding-left:6px;font-size:14px}
.f-contact div{display:flex;gap:16px;align-items:flex-start;margin-bottom:14px;line-height:20px}
.f-divider{left:98px;top:338px;width:1025px;height:1px;background:var(--line)}
.copyright{left:0;top:356px;width:1200px;text-align:center;font-size:12px}
</style>
</head>
<body>

<header class="site-nav">
  <div class="brand"><span class="brand-dot"></span><span class="brand-name">Birchmont</span></div>
  <nav class="nav-links">
    <span class="active">Services</span><span>About Us</span><span>FAQs</span><span>Employment</span><span>Testimonials</span><span>Gallery</span>
  </nav>
  <a class="btn btn-solid nav-cta">Contact Us</a>
</header>

<section class="hero" role="img" aria-label="Lake water surface with a boat hull at the edge">
  <p class="hero-eyebrow">WELCOME TO BIRCHMONT</p>
  <h1 class="hero-title">WE KNOW THERE IS NO LIFE<br>LIKE THE LAKE LIFE</h1>
  <a class="btn btn-orange hero-btn">FREE ESTIMATE</a>
</section>

<div class="feature" style="left:149px;top:612px;width:330px;height:330px" role="img" aria-label="Blue tinted lake view">
  <h3><span>FREE</span>ESTIMATE</h3>
  <p>From entry level to Nitrox courses, we can help you explore underwater.</p>
  <svg width="36" height="36" viewBox="0 0 36 36"><circle cx="18" cy="18" r="15" fill="none" stroke="#fff" stroke-width="2.5"/><path d="M11 15l7 7 7-7" fill="none" stroke="#fff" stroke-width="2.5"/></svg>
</div>
<div class="feature" style="left:761px;top:612px;width:330px;height:330px" role="img" aria-label="Blue tinted dock on a lake">
  <h3><span>BEFORE &amp;</span>AFTER GALLERY</h3>
  <p>From entry level to Nitrox courses, we can help you explore underwater.</p>
  <svg width="36" height="36" viewBox="0 0 36 36"><circle cx="18" cy="18" r="15" fill="none" stroke="#fff" stroke-width="2.5"/><path d="M11 15l7 7 7-7" fill="none" stroke="#fff" stroke-width="2.5"/></svg>
</div>
<div class="feature main" style="left:453px;top:607px;width:332px;height:332px" role="img" aria-label="Blue tinted dock and shoreline">
  <h3>DOCK INSTALL AND<br>REMOVAL SERVICES</h3>
  <p>From entry level to Nitrox courses, we can help you explore underwater.</p>
  <svg width="36" height="36" viewBox="0 0 36 36"><circle cx="18" cy="18" r="15" fill="none" stroke="#fff" stroke-width="2.5"/><path d="M11 15l7 7 7-7" fill="none" stroke="#fff" stroke-width="2.5"/></svg>
</div>

<div class="abs about-media" role="img" aria-label="Sunset over a lake seen from a dock">
  <svg class="abs" style="left:203px;top:128px" width="70" height="70" viewBox="0 0 70 70"><circle cx="35" cy="35" r="30" fill="none" stroke="#fff" stroke-width="4"/><path d="M28 22l20 13-20 13z" fill="#fff"/></svg>
</div>
<h2 class="abs heading about-title">Aquatic Innovators,<br>at Your Service.<span class="rule"></span></h2>
<p class="abs about-copy">Birchmont LLC is a company formed in response to the increasing incidence of invasive species in Minnesota's lakes and water systems. The impact of these fast-growing nuisances, inspired our venture to effectively control unwanted lake weeds. Birchmont, LLC helps provide the enjoyable weed-free lake environment craved by water enthusiasts.</p>
<a class="btn btn-solid about-btn">LEARN MORE</a>

<section class="services">
  <h2 class="heading section-title" style="top:56px">Dock Install and Removal Services<span class="rule"></span></h2>

  <article class="card" style="left:108px;top:147px">
    <div class="photo" role="img" aria-label="Zebra mussels on a rock" style="background:linear-gradient(135deg,#8a7a5e,#b59b6d 50%,#6b5a40)"></div>
    <h4>ZEBRA MUSSEL REMOVAL</h4>
    <p>Lorem Ipsum is simply dummy text of the printing and typesetting industry. Lorem Ipsum has been the industry's</p>
    <a class="btn btn-outline">LEARN MORE</a>
  </article>
  <article class="card" style="left:438px;top:147px">
    <div class="photo" role="img" aria-label="Canopy cabana on a sandy beach" style="background:linear-gradient(180deg,#d7e4ee,#a9c4d6 45%,#d9c7a6 75%,#c8b28e)"></div>
    <h4>CANOPY SERVICES</h4>
    <p>Lorem Ipsum is simply dummy text of the printing and typesetting industry. Lorem Ipsum has been the industry's</p>
    <a class="btn btn-outline">LEARN MORE</a>
  </article>
  <article class="card" style="left:770px;top:147px">
    <div class="photo" role="img" aria-label="Work barge on a trailer" style="background:linear-gradient(180deg,#c9d6e2,#9aa3a8 50%,#8d8a78)"></div>
    <h4 style="margin-top:14px">BARGE SERVICES<br>(FALL 2022)</h4>
    <p style="margin-top:4px">Lorem Ipsum is simply dummy text of the printing and typesetting industry</p>
    <a class="btn btn-outline">LEARN MORE</a>
  </article>

  <article class="card" style="left:111px;top:576px">
    <div class="photo" role="img" aria-label="Dock lifts with boats on a lake" style="background:linear-gradient(180deg,#2f78d0,#8bb8e6 40%,#3d6a9a 65%,#24508a)"></div>
    <h4 style="margin-top:18px">DOCK LIFT SERVICES<br>(FALL 2022)</h4>
    <p style="margin-top:4px">Lorem Ipsum is simply dummy text of the printing and typesetting industry</p>
    <a class="btn btn-outline">LEARN MORE</a>
  </article>
  <article class="card" style="left:441px;top:576px">
    <div class="photo" role="img" aria-label="Divers among lily pads" style="background:linear-gradient(180deg,#5b7a3e,#43632f 60%,#374f2a)"></div>
    <h4 style="margin-top:18px">AQUATIC WEED<br>REMOVAL</h4>
    <p style="margin-top:4px">Lorem Ipsum is simply dummy text of the printing and typesetting industry</p>
    <a class="btn btn-outline">LEARN MORE</a>
  </article>
  <article class="card" style="left:773px;top:576px">
    <div class="photo" role="img" aria-label="Beach clean up with a trash bag" style="background:linear-gradient(135deg,#cdb69a,#bfa88a 55%,#a9947a)"></div>
    <h4 style="margin-top:18px">BEACH CLEAN<br>UP SERVICES</h4>
    <p style="margin-top:4px">Lorem Ipsum is simply dummy text of the printing and typesetting industry</p>
    <a class="btn btn-outline">LEARN MORE</a>
  </article>

  <a class="btn btn-solid view-all">VIEW ALL SERVICES</a>
</section>

<h2 class="heading section-title" style="top:2634px;font-size:33px">Before &amp; After Gallery<span class="rule"></span></h2>
<div class="slide" style="left:113px;top:2770px;width:249px;height:240px;background:linear-gradient(180deg,#8fb6e2,#4f7fb8 55%,#2a5a96)" role="img" aria-label="Dock with boat lift on a lake"></div>
<div class="slide" style="left:841px;top:2778px;width:226px;height:240px;background:linear-gradient(90deg,#8a9a5a,#5f7a68 30%,#4e6f6a)" role="img" aria-label="Shoreline with weeds in the water"></div>
<div class="slide" style="left:362px;top:2736px;width:240px;height:307px;background:linear-gradient(180deg,#e6ebee,#5f7a45 40%,#8a8a6a 75%,#6f6a5a)" role="img" aria-label="Dock covered in lake weeds before cleaning"></div>
<div class="slide" style="left:604px;top:2736px;width:237px;height:307px;background:linear-gradient(180deg,#e6ebee,#4f7a38 40%,#a9a08a 75%,#8a8270)" role="img" aria-label="Clean dock after weed removal"></div>
<svg class="abs" style="left:576px;top:2860px" width="52" height="52" viewBox="0 0 52 52"><circle cx="26" cy="26" r="22" fill="none" stroke="#fff" stroke-width="2.5"/><path d="M22 19l-7 7 7 7M30 19l7 7-7 7" fill="none" stroke="#fff" stroke-width="2.5"/></svg>
<svg class="arrow" style="left:58px;top:2870px" width="28" height="50" viewBox="0 0 28 50"><path d="M24 3L4 25l20 22" fill="none" stroke="#9aa6b4" stroke-width="2.5"/></svg>
<svg class="arrow" style="left:1090px;top:2870px" width="28" height="50" viewBox="0 0 28 50"><path d="M4 3l20 22L4 47" fill="none" stroke="#9aa6b4" stroke-width="2.5"/></svg>

<section class="testimonials" role="img" aria-label="Blue tinted forest and lake backdrop">
  <h2 class="heading section-title" style="top:66px">Testimonials<span class="rule" style="border-top-color:#fff;border-bottom-color:rgba(255,255,255,.5)"></span></h2>
  <div class="quote-card">
    <p class="quote-text">Everyone used to jump off the water trampoline and instantly get tangled in lake weeds. We contacted Birchmont and their SCUBA divers have now been solving our problem for the past 4 years!"</p>
    <p class="quote-name">Harlow Pines Association</p>
    <p class="quote-place">(Lake Wrenwood)</p>
    <svg class="abs" style="left:280px;top:220px" width="50" height="22" viewBox="0 0 50 22"><path d="M10 4l-6 7 6 7" fill="none" stroke="#b8c0ca" stroke-width="2"/><path d="M38 4l6 7-6 7" fill="none" stroke="#1f2a3a" stroke-width="2.5"/></svg>
  </div>
  <div class="quote-badge"><svg width="26" height="20" viewBox="0 0 26 20"><path d="M2 18v-8c0-5 3-8 8-9v3c-3 1-4 3-4 5h4v9zM15 18v-8c0-5 3-8 8-9v3c-3 1-4 3-4 5h4v9z" fill="#fff"/></svg></div>
</section>

<section class="contact" role="img" aria-label="Faded misty lake backdrop">
  <h2 class="abs heading contact-title">Contact Us<span class="rule"></span></h2>
  <p class="abs contact-intro">Lorem Ipsum is simply dummy text of the printing and typesetting industry Lorem Ipsum.</p>
  <div class="info-row" style="top:260px">
    <span class="info-icon"><svg width="24" height="24" viewBox="0 0 24 24"><path d="M6 2l4 4-2 3c1 3 4 6 7 7l3-2 4 4-3 3C10 21 3 14 3 5z" fill="#fff"/></svg></span>
    <div><p class="info-label">PHONE NUMBER</p><p class="info-value">+47 900 12 345</p></div>
  </div>
  <div class="info-row" style="top:340px">
    <span class="info-icon"><svg width="26" height="20" viewBox="0 0 26 20"><rect x="1" y="1" width="24" height="18" rx="2" fill="#fff"/><path d="M2 3l11 8 11-8" fill="none" stroke="#0d5bb5" stroke-width="2"/></svg></span>
    <div><p class="info-label">ADDRESS</p><p class="info-value">4410 Fernbrook Lane<br>Millbrook, MN 55000</p></div>
  </div>
  <form class="form-card">
    <div class="field" style="top:38px"><svg width="14" height="14" viewBox="0 0 14 14"><circle cx="7" cy="4" r="3" fill="#9aa6b4"/><path d="M1 14c0-4 3-6 6-6s6 2 6 6z" fill="#9aa6b4"/></svg>Your Name</div>
    <div class="field" style="top:92px"><svg width="14" height="14" viewBox="0 0 24 24"><path d="M6 2l4 4-2 3c1 3 4 6 7 7l3-2 4 4-3 3C10 21 3 14 3 5z" fill="#9aa6b4"/></svg>Phone number</div>
    <div class="field" style="top:146px"><svg width="15" height="12" viewBox="0 0 26 20"><rect x="1" y="1" width="24" height="18" fill="#9aa6b4"/><path d="M2 3l11 8 11-8" fill="none" stroke="#fff" stroke-width="2"/></svg>Email address</div>
    <div class="field area" style="top:200px">Message</div>
    <a class="btn btn-orange form-btn">LEARN MORE</a>
  </form>
</section>

<footer class="footer">
  <div class="abs brand f-brand"><span class="brand-dot"></span><span class="brand-name">Birchmont</span></div>
  <p class="abs f-about">Birchmont LLC is a company formed in response to the increasing incidence of invasive species in Minnesota's lakes and water systems.</p>
  <div class="abs socials"><span></span><span></span><span></span><span></span></div>

  <div class="abs" style="left:493px;top:68px">
    <h4 class="f-col-title">QUICK LINKS</h4>
    <div class="f-links"><span>Home</span><span>FAQs</span><span>Services</span><span>Employment</span><span>About Us</span><span>Testimonials</span><span>Contact Us</span><span>Gallery</span></div>
  </div>
  <div class="abs" style="left:839px;top:68px">
    <h4 class="f-col-title">CONTACT US</h4>
    <div class="f-contact">
      <div><svg width="16" height="20" viewBox="0 0 16 20"><path d="M8 1a7 7 0 017 7c0 5-7 11-7 11S1 13 1 8a7 7 0 017-7z" fill="#7b8290"/><circle cx="8" cy="8" r="2.5" fill="#fff"/></svg><span>4410 Fernbrook Lane<br>Millbrook, MN 55000</span></div>
      <div><svg width="16" height="13" viewBox="0 0 26 20"><rect x="1" y="1" width="24" height="18" fill="#7b8290"/><path d="M2 3l11 8 11-8" fill="none" stroke="#fff" stroke-width="2"/></svg><span>hello@birchmont.example</span></div>
      <div><svg width="16" height="16" viewBox="0 0 24 24"><path d="M6 2l4 4-2 3c1 3 4 6 7 7l3-2 4 4-3 3C10 21 3 14 3 5z" fill="#7b8290"/></svg><span style="font-size:16px">(555) 014-2207</span></div>
    </div>
  </div>

  <div class="abs f-divider"></div>
  <p class="abs copyright">Copyright 2022 Birchmont LLC</p>
</footer>

</body>
</html>
```